rk ironcraft business card metallic look

revamp the existing design but want card to have a metalic look to it

Target Market(s)

construction industry

Industry/Entity Type

constrction

Contact Information for Business Card

front of card RK Ironcraft, phone 4165550193, email rk.ironcraftt@veltrano.com and instagram account; rk_ironcraft_

Font styles to use
Other font styles liked:
• masculine

Colors

Designer to choose only greyscale colors for use in the design.

Requirements
Must have
• back side RK Ironcraft then a list of everything : Siding, ACM Panels, Standing Seam,Soffit, Fascia, Gutters,Metal,Alu,inum, Viynyl, Metal Roofs and roof repairs
Nice to have
• I would like to keep the look of the existing card with the metal grids on the front
Should not have
• Need a design in two days

```html
<!DOCTYPE html>
<html lang="en">
<head>
<meta charset="utf-8">
<title>RK Ironcraft business card</title>
<link rel="stylesheet" href="https://fonts.googleapis.com/css2?family=Michroma&family=Roboto+Condensed:wght@400&display=swap">
<style>
  :root {
    --backdrop: #3a3a3c;
    --card-base: #2a2927;
    --card-band: #4b4a47;
    --rib-dark: #1e1e1d;
    --rib-light: #6d6d6b;
    --wordmark: #151515;
    --text-light: #f1f1f1;
    --text-metal: #bdbdbb;
  }
  * { margin: 0; padding: 0; box-sizing: border-box; }
  html, body { width: 1200px; height: 694px; overflow: hidden; }
  body { background: var(--backdrop); position: relative; }

  .card {
    position: absolute;
    width: 560px;
    height: 320px;
    background: var(--card-base);
    overflow: hidden;
    box-shadow: 0 14px 30px rgba(0,0,0,.45);
  }
  .card--services { left: 30px; top: 50px; }
  .card--contact { left: 610px; top: 324px; }

  .card__art { position: absolute; inset: 0; width: 560px; height: 320px; }
  .ribbed-panel { fill: url(#rib-tone); }
  .top-band { fill: var(--card-band); }

  .wordmark {
    position: absolute;
    left: 190px;
    top: 108px;
    font-family: "Michroma", sans-serif;
    font-size: 34px;
    color: var(--wordmark);
    letter-spacing: 1px;
    white-space: nowrap;
  }

  .services {
    position: absolute;
    left: 36px;
    bottom: 34px;
    font-family: "Roboto Condensed", sans-serif;
    font-size: 16px;
    line-height: 1.45;
    color: var(--text-light);
    text-align: center;
    width: 490px;
  }

  .social {
    position: absolute;
    right: 34px;
    top: 168px;
    display: flex;
    align-items: center;
    gap: 8px;
    font-family: "Roboto Condensed", sans-serif;
    font-size: 19px;
    color: var(--text-metal);
  }
  .social__dot {
    width: 16px; height: 16px;
    border-radius: 50%;
    border: 2px solid var(--text-metal);
  }

  .contacts {
    position: absolute;
    left: 40px;
    bottom: 30px;
    font-family: "Roboto Condensed", sans-serif;
    font-size: 20px;
    color: var(--text-metal);
    list-style: none;
  }
  .contacts li { display: flex; align-items: center; gap: 12px; margin-top: 8px; }
  .contacts svg { width: 20px; height: 20px; fill: none; stroke: var(--text-metal); stroke-width: 2; stroke-linejoin: round; stroke-linecap: round; }
</style>
</head>
<body>
  <svg width="0" height="0" style="position:absolute">
    <defs>
      <linearGradient id="rib-tone" x1="0" y1="0" x2="1" y2="0">
        <stop offset="0" stop-color="#2a2a29"/>
        <stop offset=".5" stop-color="#4a4a48"/>
        <stop offset="1" stop-color="#262625"/>
      </linearGradient>
    </defs>
  </svg>

  <section class="card card--services" aria-label="Card back: services">
    <svg class="card__art" viewBox="0 0 560 320">
      <polygon class="top-band" points="225,0 560,0 560,28 300,70"/>
      <polygon class="ribbed-panel" role="img" aria-label="Ribbed metal panel texture" points="0,0 225,0 105,220 0,220"/>
    </svg>
    <div class="wordmark">RK Ironcraft</div>
    <p class="services">• Siding • ACM Panels • Standing Seam • Soffit • Fascia • Gutters<br>• Metal • Aluminum • Vinyl • Metal Roof and Roofing Repairs</p>
  </section>

  <section class="card card--contact" aria-label="Card front: contact">
    <svg class="card__art" viewBox="0 0 560 320">
      <polygon class="top-band" points="225,0 560,0 560,28 300,70"/>
      <polygon class="ribbed-panel" role="img" aria-label="Ribbed metal panel texture" points="0,0 225,0 105,220 0,220"/>
    </svg>
    <div class="wordmark">RK Ironcraft</div>
    <div class="social"><span class="social__dot"></span><span>rk_ironcraft_</span></div>
    <ul class="contacts">
      <li>
        <svg viewBox="0 0 24 24"><path d="M5 3h4l2 5-2.5 1.5a11 11 0 0 0 6 6L16 13l5 2v4a2 2 0 0 1-2 2A16 16 0 0 1 3 5a2 2 0 0 1 2-2z"/></svg>
        <span>416-555-0193</span>
      </li>
      <li>
        <svg viewBox="0 0 24 24"><rect x="3" y="5" width="18" height="14" rx="1"/><path d="M3 6l9 7 9-7"/></svg>
        <span>rk.ironcraftt@veltrano.com</span>
      </li>
    </ul>
  </section>
</body>
</html>
```